Card Design Project

Gift Card and Gift Card Carrier Design for Spanish Tapas Restaurant/Bar

all of our current logos are on this link:
www.corvo-la-mesa.com/logos.html

you can see the different files, simply click on them to download what you need

the current name of our restaurant is: Corvo-la-mesa's Tapas Bar
we are moving to a new location and we are changing the spelling of our name to:
Valdoreno Tapas Bar

the font that our name is written in is: Mistral

in regards to the tone of the artwork, the look, the feel:
we are Spain Europe Tapas Cuisine.
Our restaurant has two ambiances
one ambiance is a rustic spanish feel on the first floor.
the second ambiance is a trendy ibiza moorish spanish feel.
go to this link for design elements of our new location
http://www.corvo-la-mesa.com/DesignConcepts.html
this is our facebook page:
http://www.facebook.com/corvolamesa

Must provide your actual design files with layers (including all font);
Adobe AI CS4 or lower or
Adobe Photoshop CS4 file or lower

Target Market(s)

ages 25 to 45 is our biggest demographic of customer

Industry/Entity Type

Restaurant

Requirements
Must have
• the front of the gift card is the actual design
the back of the gift card must be the disclaimers for the card

here are the disclaimers:

Additional value may be added to this card at any time.
We are not reponsible for lost, stolen, or damaged cards or any unauthorized card use.
Cards that are lost, stolen, or damaged cannot be replaced and have no value.
Cards cannot be redeemed for cash and cannot be used toward tax and tips.
Card expires 180 calendar days after issue date.

Valdoreno Tapas Bar
2817 West Pellham Street, Chicago IL 60641

i attached samples of the backs of other cards so you can see some samples

Hints to submit a winning design:

In regards to the Logo that we provided you, you will notice the word Valdoreno.
Feel free to not have the word Valdoreno on the front of your gift card inside the logo.
You can remove the layer and only use the logo of the flamenco dancer herself.
If you feel the word Valdoreno goes with your design then keep it.
That logo has become a brand for this restaurant and people know the brand by simply looking at the flamenco lady - so it could be used with the name Valdoreno or without the name Valdoreno.
Feel free to use patterned backgrounds on the front of the card rather than solids
Also, use a different font other than mistral for any other words that you use.
If you use the words Gift Card - use another font for that. If you decide to put the wording: Tapas Bar in your design, or Tapas - use another font, do not use mistral for that wording.

in regards to colors, this restaurant has two ambiances, one is a earthy rustic spanish and another is a loungey darker trendy elegant ambiance, - if you submit really super bright colors all over your card, the super bright features of the card is a bit contradictory to the style of the restaurant.

stay with subtle color shifts and simplicity is the key.

I am going to add a photo of the food delivery bag of the restaurant.
Their food delivery bag is a matte black color bag with a red foil stamp of the flamenco lady logo - it is simple , to the point, and everyone loves the bag when they receive it with their deliveries.

They are also considering to purchase matte black gift cards because they want to do a foil stamped gift card also - so if you use a black background in your design - that can be advantageous to winning the first choice here.

```html
<!DOCTYPE html>
<html lang="en">
<head>
<meta charset="utf-8">
<title>Valdoreno Tapas Bar Gift Card Carrier</title>
<link rel="stylesheet" href="https://fonts.googleapis.com/css2?family=Arimo&family=Cabin:wght@700&display=swap">
<style>
  :root {
    --paper-light: #ecdcb4;
    --paper-mid: #dcc394;
    --paper-edge: #a98752;
    --brand-red: #c1141d;
    --ink: #2a2016;
    --white: #ffffff;
  }
  html, body {
    margin: 0;
    padding: 0;
    overflow: hidden;
    background: var(--white);
  }
  .canvas {
    position: relative;
    width: 1200px;
    height: 872px;
    overflow: hidden;
    background: var(--white);
  }
  .panel {
    position: absolute;
    top: 0;
    height: 872px;
    overflow: hidden;
    background:
      radial-gradient(ellipse 75% 65% at 50% 45%, var(--paper-light) 0%, var(--paper-mid) 60%, var(--paper-edge) 100%);
  }
  .panel--outside { left: 0; width: 544px; }
  .panel--inside { left: 654px; width: 546px; }

  .greeting-band {
    position: absolute;
    left: 0;
    top: 42px;
    width: 100%;
    height: 56px;
    background: var(--brand-red);
    display: flex;
    align-items: center;
    justify-content: center;
  }
  .greeting-band__text {
    font-family: "Cabin", sans-serif;
    font-weight: 700;
    font-size: 44px;
    color: var(--white);
    letter-spacing: 1px;
  }

  .venue-block {
    position: absolute;
    left: 0;
    top: 196px;
    width: 100%;
    transform: rotate(180deg);
    display: flex;
    flex-direction: column;
    align-items: center;
    color: var(--ink);
    font-family: "Arimo", sans-serif;
  }
  .venue-block__mark {
    width: 40px;
    height: 40px;
    border-radius: 50%;
    background: var(--ink);
    opacity: 0.75;
    margin-bottom: 14px;
  }
  .venue-block__name {
    font-size: 24px;
    margin-bottom: 8px;
  }
  .venue-block__address,
  .venue-block__web {
    font-size: 13px;
    line-height: 22px;
  }

  .recipient-form {
    position: absolute;
    left: 56px;
    top: 68px;
    width: 440px;
    font-family: "Arimo", sans-serif;
    font-size: 28px;
    color: var(--ink);
  }
  .recipient-form__row {
    display: flex;
    align-items: flex-end;
    height: 62px;
  }
  .recipient-form__label { margin-right: 8px; line-height: 1; }
  .recipient-form__line {
    flex: 1;
    border-bottom: 2px solid var(--ink);
    margin-bottom: 4px;
  }

  .footer-band {
    position: absolute;
    left: 0;
    bottom: 0;
    width: 100%;
    height: 148px;
    background: var(--brand-red);
  }
</style>
</head>
<body>
<div class="canvas">
  <section class="panel panel--outside">
    <div class="greeting-band"><span class="greeting-band__text">Enjoy!</span></div>
    <div class="venue-block">
      <div class="venue-block__mark"></div>
      <div class="venue-block__name">Valdoreno Tapas Bar</div>
      <div class="venue-block__address">2817 West Pellham Street, Chicago IL 60641</div>
      <div class="venue-block__web">www.corvo-la-mesa.com</div>
    </div>
  </section>

  <section class="panel panel--inside">
    <div class="recipient-form">
      <div class="recipient-form__row"><span class="recipient-form__label">To:</span><span class="recipient-form__line"></span></div>
      <div class="recipient-form__row"><span class="recipient-form__label">From:</span><span class="recipient-form__line"></span></div>
      <div class="recipient-form__row"><span class="recipient-form__label">Amount:</span><span class="recipient-form__line"></span></div>
    </div>
    <div class="footer-band"></div>
  </section>
</div>
</body>
</html>
```